Purl Haven planner/ book cover

PURL HAVEN" - A UNIQUE NOTEBOOK FOR CRAFTS. The main goal of a "Purl Haven" notebook is to arrange your crafts notes like knitting planner. Its pages are systematically structured, so they are easy to review, and all the information about the started project is in one place. The notebook has a click opening system, so you can remove, insert, change pages.
This is the old design in Latvian language. I want a new, classic, modern cover design for selling book in USA.I prefer original picture rather than download. Maybe for some of yourself drawings. Illustrated color-wash and minimalistic style better than photography.
Look at the pages inside design so that the lid fits. Maybe i want to change some clipart on the inside as well (just small one, like ball of yarn, sweater, can be seen in the picture, more classic style, not so childish, but that's latter), leave yoga clipart and the colors. Check please video.
https://www.examplevideo-host.com/watch?v=Qm4rT8zLk2W
www.purlhavenstudio.com its my style.

book title- purl haven
slogan- its time for sitting to do some knitting
size- 18 x 23,5 x 4 cm

Colors
d3a5cc
eea4c8
fdf2f7
fbd4d5
fdf0f6
ffffff
e34297
a64599
b868aa

```html
<!DOCTYPE html>
<html lang="en">
<head>
<meta charset="utf-8">
<title>Purl Haven — Planner Cover</title>
<link rel="stylesheet" href="https://fonts.googleapis.com/css2?family=Kaushan+Script&family=Shadows+Into+Light&display=swap">
<style>
  :root {
    --paper: #fdf5f6;
    --blush: #fbd4d5;
    --peach: #f6c3ad;
    --peach-deep: #f2b49c;
    --rose: #eea4c8;
    --rose-deep: #f0a3b6;
    --lavender: #d3a5cc;
    --lavender-soft: #dcc1e0;
    --gold: #d7b24a;
    --gold-soft: #e8cf8a;
    --ink: #2f2f30;
    --yarn-light: #f6c6ad;
    --yarn-mid: #eba889;
    --yarn-dark: #c9826a;
  }
  * { box-sizing: border-box; margin: 0; padding: 0; }
  html, body { width: 837px; height: 1200px; overflow: hidden; background: #ffffff; }
  .cover {
    position: relative;
    width: 837px;
    height: 1200px;
    overflow: hidden;
    background: var(--paper);
  }
  .wash { position: absolute; inset: 0; }
  .title {
    position: absolute;
    top: 158px;
    left: 0;
    width: 100%;
    text-align: center;
    font-family: "Kaushan Script", cursive;
    font-size: 104px;
    line-height: 1.2;
    color: var(--ink);
    letter-spacing: -1px;
  }
  .yarn-art {
    position: absolute;
    left: 208px;
    top: 360px;
    width: 440px;
    height: 432px;
    border-radius: 50%;
    background: radial-gradient(circle at 45% 40%, var(--yarn-light) 0%, var(--yarn-mid) 62%, var(--yarn-dark) 100%);
    box-shadow: 10px 40px 40px -20px rgba(140, 100, 120, 0.45);
  }
  .slogan {
    position: absolute;
    top: 866px;
    left: 0;
    width: 100%;
    text-align: center;
    font-family: "Shadows Into Light", cursive;
    font-size: 27px;
    line-height: 42px;
    color: var(--ink);
    text-transform: uppercase;
    letter-spacing: 0.5px;
  }
</style>
</head>
<body>
  <main class="cover">
    <svg class="wash" width="837" height="1200" viewBox="0 0 837 1200" aria-hidden="true">
      <defs>
        <filter id="soft" x="-30%" y="-30%" width="160%" height="160%">
          <feGaussianBlur stdDeviation="18"/>
        </filter>
        <filter id="softer" x="-30%" y="-30%" width="160%" height="160%">
          <feGaussianBlur stdDeviation="8"/>
        </filter>
        <linearGradient id="gold-stroke" x1="0" y1="0" x2="0" y2="1">
          <stop offset="0" stop-color="var(--gold)" stop-opacity="0.85"/>
          <stop offset="1" stop-color="var(--gold-soft)" stop-opacity="0.25"/>
        </linearGradient>
      </defs>
      <g class="wash-peach" filter="url(#softer)">
        <path d="M100 0 H640 V110 C560 150 420 160 300 150 C200 140 150 120 110 80 Z" fill="var(--peach)" opacity="0.8"/>
        <ellipse cx="700" cy="60" rx="120" ry="90" fill="var(--peach)" opacity="0.45"/>
      </g>
      <path class="wash-gold-top" d="M600 0 H830 C835 60 800 160 740 240 C720 270 700 300 690 310 C680 240 610 180 595 120 Z" fill="url(#gold-stroke)" opacity="0.8"/>
      <g class="wash-rose" filter="url(#soft)">
        <ellipse cx="720" cy="720" rx="150" ry="160" fill="var(--rose-deep)" opacity="0.7"/>
        <ellipse cx="540" cy="820" rx="260" ry="90" fill="var(--blush)" opacity="0.9"/>
        <ellipse cx="200" cy="820" rx="240" ry="70" fill="var(--blush)" opacity="0.6"/>
      </g>
      <g class="wash-lavender" filter="url(#soft)">
        <ellipse cx="150" cy="940" rx="230" ry="70" fill="var(--lavender)" opacity="0.7"/>
        <ellipse cx="330" cy="1085" rx="380" ry="80" fill="var(--lavender-soft)" opacity="0.85"/>
        <ellipse cx="640" cy="1080" rx="220" ry="80" fill="var(--blush)" opacity="0.8"/>
      </g>
      <g class="wash-gold-bottom" fill="none" stroke="var(--gold-soft)" stroke-linecap="round" opacity="0.8">
        <path d="M0 1035 C180 960 380 965 520 1000" stroke-width="16"/>
        <path d="M0 1130 C150 1105 260 1120 380 1160" stroke-width="10" opacity="0.7"/>
      </g>
      <g class="gold-dots" fill="var(--gold)">
        <circle cx="30" cy="18" r="9"/><circle cx="48" cy="40" r="10"/><circle cx="68" cy="52" r="8"/>
        <circle cx="138" cy="38" r="10"/><circle cx="207" cy="38" r="9"/><circle cx="188" cy="98" r="6"/>
        <circle cx="531" cy="70" r="8"/><circle cx="545" cy="95" r="11"/><circle cx="570" cy="112" r="10"/>
        <circle cx="650" cy="95" r="6"/><circle cx="712" cy="88" r="7"/><circle cx="695" cy="152" r="6"/>
        <circle cx="760" cy="1095" r="3"/><circle cx="790" cy="1070" r="3"/><circle cx="735" cy="1130" r="2.5"/>
        <circle cx="800" cy="1150" r="3"/><circle cx="700" cy="1165" r="2"/><circle cx="812" cy="1040" r="2"/>
      </g>
    </svg>

    <h1 class="title">Purl Haven</h1>

    <div class="yarn-art" role="img" aria-label="Watercolour ball of peach yarn with two knitting needles pushed through it"></div>

    <p class="slogan">Its time for sitting to do<br>some knitting</p>
  </main>
</body>
</html>
```